Classy business card for accounting firm

We're looking for a new business card for our accounting firm. Our logo was designed by Brandloom, so all of the design info we would like to use has been provided. The specific font provided isn't required to be used.

We want the card to look classy and elegent. Probably more minimalistic, but still with some pops of color.

The options we would like to include on the card are as follows:
1. Main office phone line
2. Direct phone line
3. Email address
4. Website URL
5. Name
6. Title (CEO, President, etc.)
7. Firm Address

The design and card should be double sided!!! The drop down box in the project brief for some reason is defaulting to single sided. Not sure why this is happening.

Thanks!

Contact Information for Business Card

The options we would like to include on the card are as follows: 1. Main office phone line 2. Direct phone line 3. Email address 4. Website URL 5. Name 6. Title (CEO, President, etc.) 7. Firm Address

Requirements
Must have
• Card must be double sided.

```html
<!DOCTYPE html>
<html lang="en">
<head>
<meta charset="utf-8">
<title>Brightfield Associates – Business Card</title>
<link rel="stylesheet" href="https://fonts.googleapis.com/css2?family=Montserrat:wght@500;600&family=Arimo:wght@400;700&display=swap">
<style>
  :root {
    --bg: #1d1d1f;
    --card-white: #ffffff;
    --card-dark: #2a2a2c;
    --card-dark-2: #3a3a3c;
    --orange: #f47a14;
    --green: #9bb83a;
    --ink: #4a4a4a;
    --ink-soft: #6b6b6b;
  }
  * { box-sizing: border-box; margin: 0; padding: 0; }
  html, body { width: 1200px; height: 900px; overflow: hidden; }
  body {
    background: var(--bg);
    display: flex;
    align-items: center;
    justify-content: center;
    gap: 40px;
  }
  .card {
    width: 525px;
    height: 300px;
    border-radius: 22px;
    position: relative;
    overflow: hidden;
  }

  /* Front */
  .card-front { background: var(--card-white); padding: 34px 36px 0; }
  .brand { text-align: center; }
  .brand-square {
    width: 30px; height: 30px;
    background: var(--orange);
    margin: 0 auto 12px;
  }
  .brand-name-row {
    display: flex; align-items: center; justify-content: center; gap: 14px;
  }
  .brand-rule { width: 40px; height: 2px; background: var(--green); }
  .brand-name {
    font-family: "Montserrat", sans-serif;
    font-weight: 500;
    font-size: 30px;
    letter-spacing: 1px;
    color: var(--ink);
  }
  .brand-tagline {
    font-family: "Montserrat", sans-serif;
    font-weight: 600;
    font-size: 11px;
    letter-spacing: 2.5px;
    color: var(--ink);
    margin-top: 4px;
  }
  .details {
    display: flex;
    margin-top: 30px;
    font-family: "Arimo", sans-serif;
  }
  .person { flex: 1; text-align: right; padding-right: 20px; }
  .person-name {
    font-weight: 700; font-size: 19px; color: var(--orange); text-transform: uppercase;
  }
  .person-title, .person-address {
    font-size: 14px; color: var(--ink-soft); line-height: 1.35;
  }
  .person-title { margin-bottom: 4px; }
  .divider { width: 2px; background: #9a9a9a; }
  .contacts { flex: 1.15; padding-left: 18px; list-style: none; }
  .contact {
    display: flex; align-items: center; gap: 8px;
    font-size: 14.5px; color: var(--ink-soft); line-height: 1.45;
  }
  .contact svg { width: 13px; height: 13px; flex: none; }

  /* Back */
  .card-back { background: var(--card-dark); }
  .back-texture {
    position: absolute; inset: 0;
    background: linear-gradient(135deg, #202022 0%, var(--card-dark) 45%, var(--card-dark-2) 100%);
  }
  .back-brand {
    position: absolute; left: 0; right: 0; top: 50%;
    transform: translateY(-50%);
    display: flex; align-items: center; justify-content: center; gap: 10px;
  }
  .back-brand .brand-square { margin: 0; width: 22px; height: 22px; }
  .back-brand-name {
    font-family: "Montserrat", sans-serif;
    font-weight: 500; font-size: 20px; letter-spacing: 1px;
    color: var(--orange);
  }
</style>
</head>
<body>

<section class="card card-front" aria-label="Card front">
  <header class="brand">
    <div class="brand-square"></div>
    <div class="brand-name-row">
      <span class="brand-rule"></span>
      <h1 class="brand-name">BRIGHTFIELD ASSOCIATES</h1>
      <span class="brand-rule"></span>
    </div>
    <p class="brand-tagline">SOLVING TAX PROBLEMS</p>
  </header>

  <div class="details">
    <div class="person">
      <p class="person-name">Daniel Carter</p>
      <p class="person-title">CEO, President</p>
      <p class="person-address">Your Address, City<br>State, Zip 0000</p>
    </div>
    <div class="divider"></div>
    <ul class="contacts">
      <li class="contact">
        <svg viewBox="0 0 16 16" aria-hidden="true"><path fill="var(--orange)" d="M3.5 1.5l2.5 0 1 3.5-1.6 1.2a8 8 0 0 0 4.4 4.4L11 9l3.5 1v2.5c0 1-1 2-2 2A11 11 0 0 1 1.5 3.5c0-1 1-2 2-2z"/></svg>
        555-014-2100
      </li>
      <li class="contact">
        <svg viewBox="0 0 16 16" aria-hidden="true"><rect x="4" y="1" width="8" height="14" rx="1.5" fill="none" stroke="var(--orange)" stroke-width="1.6"/><circle cx="8" cy="12.3" r="0.9" fill="var(--orange)"/></svg>
        555-014-2101
      </li>
      <li class="contact">
        <svg viewBox="0 0 16 16" aria-hidden="true"><rect x="1.5" y="3.5" width="13" height="9" fill="none" stroke="var(--orange)" stroke-width="1.6"/><path d="M1.5 3.5L8 9l6.5-5.5" fill="none" stroke="var(--orange)" stroke-width="1.6"/></svg>
        hello@brightfieldtax.com
      </li>
      <li class="contact">
        <svg viewBox="0 0 16 16" aria-hidden="true"><circle cx="8" cy="8" r="6.5" fill="none" stroke="var(--orange)" stroke-width="1.5"/><ellipse cx="8" cy="8" rx="2.8" ry="6.5" fill="none" stroke="var(--orange)" stroke-width="1.2"/><path d="M1.5 8h13M2.6 4.6h10.8M2.6 11.4h10.8" stroke="var(--orange)" stroke-width="1.2"/></svg>
        www.brightfieldtax.com
      </li>
    </ul>
  </div>
</section>

<section class="card card-back" aria-label="Card back">
  <div class="back-texture" role="img" aria-label="Tonal embossed repeat pattern of the brand symbol across the dark card back"></div>
  <div class="back-brand">
    <span class="brand-square"></span>
    <span class="back-brand-name">BRIGHTFIELD ASSOCIATES</span>
  </div>
</section>

</body>
</html>
```